Security and Technology Website - Bold and Confident, Something Unexpected

Silver Heron Systems is launching its first website and we need a great design to bring our brand to life and generate DTC and B2B leads.

We have a good logo, but I am struggling with the creative vision to bring it all together. While our industry is Alarm Systems and Technology, we want to create a site that is more friendly and less 'typical' than your standard IT sites.

It Must:
1. Appeal to both men and women. The logo is a bit masculine, so the colors and icons must soften this.
2. Feel modern - we need to convey that we we use the latest technology.
3. Feel a bit high-end. We are not a budget solution.
4. Have a distinct iconography and photo treatment.
5. Feel layered - not just a series of stacked horizontal modules.

It Should Not:
1. Feel like your typical IT website.

Here are resources to get you started!
• Staging Site:
https://silver-heron-systems.examplestore.test/
Password: Pippa

•Brand Guide: https://www.sketchboardly.test/design/QWRtLmPOx4K/vBnm8Kq2-ZXyTrLp7hd-QE/edit?utm_content=QWRtLmPOx4K&utm_campaign=designshare&utm_medium=link2&utm_source=sharebutton

• Logo and Fonts and Photos: :https://files.cloudvaultia.test/folders/7KpWmQ3xNrT8yLbZ2vHcJ5dFg9sAeUoPi?usp=sharing

• Design Inspiration (don't feel limited by this): https://www.sketchboardly.test/design/HJkPqRvBn2s/m7TyUiOp4LkJhGfDsA2-ZX/edit?utm_content=HJkPqRvBn2s&utm_campaign=designshare&utm_medium=link2&utm_source=sharebutton

______________

The winner will be asked to provide design files and finished PNGs of the overall design file, backgrounds, photo treatments/frames, and icons.

The winner will likely be engaged for a phase 2 to build out a product page.

Industry/Entity Type

Alarm Systems, Home Theatres, and Commercial IT Networking

Number of Pages Required

1 page

Font styles to use
Sans Serif

Colors
0054AA
0677BA
7BADD7
CADEEF
E8F1F8
0094D4
00A9DD
6FCCEA
C7EBF8
E9F6FB
EB3D1F
EC4F4E
F09395
F8D3D4
FCEDEE

Requirements
Must have
• 1. Appeal to both men and women. The logo is a bit masculine, so the colors and icons must soften this. 2. Feel modern - we need to convey that we we use the latest technology. 3. Feel a bit high-end. We are not a budget solution. 4. Have a distinct iconography and photo treatment. 5. Feel layered - not just a series of stacked horizontal modules.
Should not have
• 1. Should not feel like just another IT website.

```html
<!DOCTYPE html>
<html lang="en">
<head>
<meta charset="utf-8">
<title>Silver Heron Systems — Safer. Smarter. Faster.</title>
<link href="https://fonts.googleapis.com/css2?family=Saira:wght@600;700;800;900&family=Poppins:wght@400;500;600;700&display=swap" rel="stylesheet">
<style>
:root{
  --navy:#0f4c8a;
  --blue:#0054AA;
  --blue-mid:#0677BA;
  --sky:#7bc8e8;
  --sky-soft:#CADEEF;
  --pale:#e3f3fa;
  --pale-2:#E9F6FB;
  --red:#e0141c;
  --red-dark:#c20f16;
  --ink:#1b1b1b;
  --muted:#444;
  --gold:#f4b400;
  --white:#fff;
}
*{box-sizing:border-box;margin:0;padding:0}
html,body{width:1200px;height:4688px;overflow:hidden}
body{position:relative;font-family:"Poppins",sans-serif;color:var(--ink);background:var(--white)}
.abs{position:absolute}
.head{font-family:"Saira",sans-serif;font-weight:800;letter-spacing:.2px;color:#111}
.center{text-align:center}

/* header */
.topbar{left:451px;top:0;width:749px;height:33px;background:var(--navy);clip-path:polygon(18px 0,100% 0,100% 100%,0 100%);color:#fff;font-size:10px;font-weight:600}
.topbar span{position:absolute;top:10px}
.topbar .soc{width:11px;height:11px;border:2px solid #fff;border-radius:2px;top:11px}
.brand{left:88px;top:10px;width:120px;color:var(--blue);font-family:"Poppins",sans-serif;font-weight:700;font-size:14px;line-height:16px;display:flex;gap:7px;align-items:center}
.brand i{display:block;width:14px;height:14px;background:var(--red);flex:none}
.nav{top:62px;left:490px;display:flex;gap:26px;font-size:10px;font-weight:600;color:#222;align-items:center}
.nav .car::after{content:"";display:inline-block;width:5px;height:5px;border-right:1.5px solid #222;border-bottom:1.5px solid #222;transform:rotate(45deg);margin:0 0 2px 7px}

/* hero */
.hero-bg{left:0;top:100px;width:1200px;height:700px;background:linear-gradient(180deg,#eaf6fb 0%,#ffffff 55%)}
.tag{top:287px;width:1200px;font-size:19px;color:#333}
.h-safer{top:300px;width:1200px;font-size:100px;line-height:120px;color:var(--navy);font-weight:900}
.h-smart{top:392px;width:1200px;font-size:70px;line-height:80px;font-weight:900}
.h-smart .r{color:var(--red)}.h-smart .b{color:var(--navy)}
.h-hb{top:462px;width:1200px;font-size:34px;line-height:40px;color:var(--navy);font-weight:800}
.photo-l{left:167px;top:662px;width:258px;height:300px;border-radius:0 70px 0 0;background:linear-gradient(160deg,#e9ddd2,#b99a85 60%,#8c6a58)}
.frame-l{left:177px;top:655px;width:248px;height:300px;border:2px solid var(--red);border-radius:0 70px 0 0}
.photo-c{left:447px;top:656px;width:304px;height:304px;border-radius:50%;background:radial-gradient(circle at 50% 45%,#d8cdbf,#9b8a77 60%,#5d5046)}
.ring-c{left:437px;top:648px;width:320px;height:320px;border-radius:50%;border:2px solid var(--sky)}
.photo-r{left:775px;top:652px;width:259px;height:312px;background:linear-gradient(170deg,#eef0ee,#b9c3c0 50%,#3d7a3a)}
.frame-r{left:782px;top:658px;width:245px;height:306px;border:2px solid var(--navy)}
.cap{top:982px;font-size:11.5px;line-height:20px;color:#333}
.cap b{font-family:"Saira",sans-serif;font-weight:800;font-size:14px;color:#111;display:block;margin-bottom:2px}

/* features */
.sec-title{font-size:34px;line-height:40px;width:1200px;text-align:center}
.feat{top:1226px;width:190px;text-align:center}
.feat svg{display:block;margin:0 auto}
.feat h4{font-family:"Saira",sans-serif;font-weight:800;font-size:13.5px;margin-top:16px;color:#111;white-space:nowrap}
.feat p{font-size:11.5px;line-height:19px;color:#444;margin-top:3px}

/* monitoring */
.band{left:0;top:1511px;width:1200px;height:196px;background:linear-gradient(90deg,var(--navy) 55%,#1a5c9c 100%);overflow:hidden}
.band h3{left:275px;top:55px;font-size:34px;color:#fff;font-weight:800}
.band p{left:275px;top:100px;width:520px;font-size:12px;line-height:20px;color:#fff}
.btn-red{background:var(--red);color:#fff;font-size:11px;font-weight:700;display:flex;align-items:center;justify-content:center;clip-path:polygon(0 0,100% 0,88% 100%,0 100%)}

/* steps */
.steps-h{left:135px;top:1882px;font-size:33px;line-height:45px}
.step{left:572px;width:500px;display:flex;gap:18px}
.step .num{flex:none;width:64px;height:76px;display:flex;align-items:center;justify-content:center;color:#fff;font-family:"Saira",sans-serif;font-weight:800;font-size:25px;clip-path:path("M0 8 Q32 -6 64 8 L64 40 Q64 66 32 76 Q0 66 0 40 Z")}
.step h5{font-family:"Saira",sans-serif;font-weight:800;font-size:13.5px;margin-top:4px}
.step p{font-size:12px;line-height:20px;color:#333;margin-top:3px}
.step a{display:block;color:var(--blue-mid);font-size:11.5px;font-weight:600;margin-top:6px;text-decoration:none}

/* founder */
.founder{left:0;top:2166px;width:1200px;height:568px;background:var(--pale)}
.founder h2{left:122px;top:122px;font-size:33px;line-height:40px;width:560px}
.founder p{left:122px;top:300px;width:560px;font-size:12.5px;line-height:20px;color:#333}
.sig{left:122px;top:390px;width:170px;height:70px;border-radius:6px;background:linear-gradient(90deg,rgba(15,76,138,.12),rgba(15,76,138,.04))}
.portrait{left:700px;top:45px;width:334px;height:466px;background:linear-gradient(180deg,#d9c2b4 0%,#b79c8d 30%,#2f4163 55%,#1f2b42 100%);clip-path:path("M40 120 Q167 95 294 120 L294 280 Q294 380 167 440 Q40 380 40 280Z")}

/* testimonials */
.t-card{left:191px;top:2897px;width:812px;height:397px;background:var(--sky)}
.t-left{left:6px;top:6px;width:415px;height:385px;background:#fff;text-align:center}
.t-right{left:421px;top:0;width:391px;height:397px;background:var(--navy)}
.t-inner{left:31px;top:28px;width:328px;height:340px;border:1px solid rgba(255,255,255,.55)}
.quote-box{left:8px;top:103px;width:56px;height:56px;background:var(--sky);color:#fff;font-family:"Saira",sans-serif;font-size:60px;font-weight:900;line-height:80px;text-align:center}
.t-text{left:79px;top:88px;width:256px;color:#fff;font-size:12.5px;line-height:20px}
.stars{color:var(--gold);letter-spacing:2px}

/* form */
.form label{position:absolute;font-size:13.5px;color:#222}
.form .field{position:absolute;border:1.5px solid #7aa7d6;background:#fff}
.form .ph{font-size:12.5px;color:#777;padding:12px 10px}

/* partners */
.partner{top:3982px;height:77px;border:1.5px solid #d6dde3;background:#fff;display:flex;align-items:center;justify-content:center}
.partner i{display:block;height:18px;background:#2b2b2b;border-radius:3px}

/* newsletter */
.news{left:0;top:4141px;width:1200px;height:182px;background:var(--red);overflow:hidden}
.news h2{left:170px;top:52px;font-size:35px;line-height:38px;color:#fff;font-weight:800}
.news p{left:170px;top:132px;font-size:11px;color:#fff}

/* footer */
.footer{left:0;top:4323px;width:1200px;height:365px;background:var(--navy);color:#fff}
.fcol{top:100px;font-size:11px;line-height:21px}
.fcol h6{font-family:"Saira",sans-serif;font-weight:800;font-size:16px;margin-bottom:12px;letter-spacing:.3px}
.fcol a{display:block;color:#fff;text-decoration:none}
</style>
</head>
<body>

<!-- header -->
<div class="abs topbar">
  <span style="left:38px"><svg width="10" height="10" viewBox="0 0 24 24" style="vertical-align:-1px;margin-right:8px"><path fill="#fff" d="M6.6 10.8a15.1 15.1 0 0 0 6.6 6.6l2.2-2.2c.3-.3.7-.4 1-.2 1.1.4 2.3.6 3.6.6.6 0 1 .4 1 1V20c0 .6-.4 1-1 1C10.6 21 3 13.4 3 4c0-.6.4-1 1-1h3.5c.6 0 1 .4 1 1 0 1.3.2 2.5.6 3.6.1.3 0 .7-.2 1z"/></svg>CONTACT US FOR A QUOTE 615.555.0142</span>
  <span style="left:311px">ABOUT</span>
  <span style="left:364px">PROJECT CONSULTING</span>
  <span style="left:497px">CONTACT</span>
  <span class="soc" style="left:624px"></span>
  <span class="soc" style="left:653px"></span>
</div>
<div class="abs brand"><i></i><span>SILVER HERON SYSTEMS</span></div>
<nav class="abs nav">
  <svg width="14" height="13" viewBox="0 0 24 22"><path fill="#0054AA" d="M12 1 1 11h3v10h6v-6h4v6h6V11h3z"/></svg>
  <span class="car" style="margin-left:10px">ELECTRONIC SECURITY</span>
  <span class="car">AUDIO + VIDEO</span>
  <span class="car">NETWORKING + COMMUNICATION</span>
  <span class="car">CABLING</span>
  <svg width="12" height="12" viewBox="0 0 24 24" style="margin-left:18px"><circle cx="10" cy="10" r="7" fill="none" stroke="#222" stroke-width="3"/><path d="m15 15 7 7" stroke="#222" stroke-width="3"/></svg>
</nav>

<!-- hero -->
<div class="abs hero-bg"></div>
<svg class="abs" style="left:0;top:100px" width="1200" height="800" viewBox="0 100 1200 800">
  <polygon points="150,210 250,210 200,300" fill="#d4eef8" opacity=".7"/>
  <polygon points="0,270 258,555 0,870 0,660 102,555 0,445" fill="var(--red)"/>
  <polygon points="1090,100 1200,100 1200,330" fill="var(--red)"/>
  <polygon points="1085,100 1200,330 1200,700 1010,400" fill="var(--red)"/>
  <polygon points="1040,100 1085,100 1010,400 1200,700 1200,745 980,410" fill="var(--navy)"/>
</svg>
<div class="abs tag center">Proudly Serving Middle Tennessee</div>
<div class="abs head h-safer center">SAFER.</div>
<div class="abs head h-smart center"><span class="r">SMARTER.</span> <span class="b">FASTER.</span></div>
<div class="abs head h-hb center">HOMES + BUSINESSES</div>

<div class="abs frame-l"></div>
<div class="abs photo-l" role="img" aria-label="Woman arming a wall-mounted home security keypad"></div>
<div class="abs ring-c"></div>
<div class="abs photo-c" role="img" aria-label="Home theatre room with wall screen and seating"></div>
<div class="abs photo-r" role="img" aria-label="Person on a video conference call in a bright office"></div>
<div class="abs frame-r"></div>

<div class="abs cap" style="left:167px"><b>AFFORDABLE SECURITY</b>For Homes • For Businesses</div>
<div class="abs cap center" style="left:449px;width:300px"><b>ENVIABLE ENTERTAINMENT</b>Home Theatres • Smart Homes<br>• Whole Home A/V</div>
<div class="abs cap" style="left:775px"><b>AFFORDABLE SECURITY</b>Conference Systems • Phones<br>• Networking • WiFi</div>

<!-- connect + protect -->
<h2 class="abs head sec-title" style="top:1127px">CONNECT + PROTECT YOUR WORLD</h2>
<p class="abs center" style="top:1177px;width:1200px;font-size:11.5px;color:#333">Protect your people, assets, and information from whatever comes.</p>

<div class="abs feat" style="left:90px">
  <svg width="90" height="106" viewBox="0 0 90 106"><path d="M45 3 Q70 12 86 8 L86 52 Q86 86 45 103 Q4 86 4 52 L4 8 Q20 12 45 3Z" fill="#d8eff8" stroke="#7bc8e8" stroke-width="3"/><path d="M45 14 Q64 21 76 18 L76 52 Q76 80 45 93 Q14 80 14 52 L14 18 Q26 21 45 14Z" fill="#fff"/><g fill="none" stroke="#0f4c8a" stroke-width="2.2"><circle cx="45" cy="50" r="5"/><path d="M36 41a13 13 0 0 0 0 18M54 41a13 13 0 0 1 0 18M30 35a21 21 0 0 0 0 30M60 35a21 21 0 0 1 0 30"/><path d="M45 55v16"/></g></svg>
  <h4>ENTRY &amp; MOTION SENSORS</h4><p>Pair text with an icon to focus on your chosen product, collection, or blog post.</p>
</div>
<div class="abs feat" style="left:306px">
  <svg width="90" height="106" viewBox="0 0 90 106"><path d="M45 3 Q70 12 86 8 L86 52 Q86 86 45 103 Q4 86 4 52 L4 8 Q20 12 45 3Z" fill="#d8eff8" stroke="#7bc8e8" stroke-width="3"/><path d="M45 14 Q64 21 76 18 L76 52 Q76 80 45 93 Q14 80 14 52 L14 18 Q26 21 45 14Z" fill="#fff"/><g fill="none" stroke="#0f4c8a" stroke-width="2.2"><rect x="34" y="30" width="22" height="40" rx="4"/><circle cx="45" cy="52" r="6"/><circle cx="45" cy="38" r="2"/></g></svg>
  <h4>VIDEO DOORBELLS</h4><p>Pair text with an icon to focus on your chosen product, collection, or blog post.</p>
</div>
<div class="abs feat" style="left:513px">
  <svg width="90" height="106" viewBox="0 0 90 106"><path d="M45 3 Q70 12 86 8 L86 52 Q86 86 45 103 Q4 86 4 52 L4 8 Q20 12 45 3Z" fill="#d8eff8" stroke="#7bc8e8" stroke-width="3"/><path d="M45 14 Q64 21 76 18 L76 52 Q76 80 45 93 Q14 80 14 52 L14 18 Q26 21 45 14Z" fill="#fff"/><g fill="none" stroke="#0f4c8a" stroke-width="2.2"><path d="M30 38l26-8 4 14-26 8z"/><path d="M44 49l2 10h-8M30 32v30"/><circle cx="52" cy="41" r="2.5"/></g></svg>
  <h4>SECURITY CAMERAS</h4><p>Pair text with an icon to focus on your chosen product, collection, or blog post.</p>
</div>
<div class="abs feat" style="left:715px">
  <svg width="90" height="106" viewBox="0 0 90 106"><path d="M45 3 Q70 12 86 8 L86 52 Q86 86 45 103 Q4 86 4 52 L4 8 Q20 12 45 3Z" fill="#d8eff8" stroke="#7bc8e8" stroke-width="3"/><path d="M45 14 Q64 21 76 18 L76 52 Q76 80 45 93 Q14 80 14 52 L14 18 Q26 21 45 14Z" fill="#fff"/><g fill="none" stroke="#0f4c8a" stroke-width="2.2"><ellipse cx="45" cy="58" rx="10" ry="8"/><circle cx="34" cy="44" r="4"/><circle cx="42" cy="37" r="4"/><circle cx="51" cy="37" r="4"/><circle cx="58" cy="45" r="4"/></g></svg>
  <h4>PET-FRIENDLY</h4><p>Pair text with an icon to focus on your chosen product, collection, or blog post.</p>
</div>
<div class="abs feat" style="left:919px">
  <svg width="90" height="106" viewBox="0 0 90 106"><path d="M45 3 Q70 12 86 8 L86 52 Q86 86 45 103 Q4 86 4 52 L4 8 Q20 12 45 3Z" fill="#d8eff8" stroke="#7bc8e8" stroke-width="3"/><path d="M45 14 Q64 21 76 18 L76 52 Q76 80 45 93 Q14 80 14 52 L14 18 Q26 21 45 14Z" fill="#fff"/><g fill="none" stroke="#0f4c8a" stroke-width="2.2"><path d="M45 30c8 10 14 17 14 27a14 14 0 0 1-28 0c0-7 4-11 7-15 1 5 3 7 5 7 0-6-1-12 2-19z"/><path d="M45 52c4 4 5 6 5 9a5 5 0 0 1-10 0c0-3 2-6 5-9z"/></g></svg>
  <h4>FIRE &amp; CARBON MONOXIDE</h4><p>Pair text with an icon to focus on your chosen product, collection, or blog post.</p>
</div>

<!-- monitoring band -->
<section class="abs band">
  <svg class="abs" style="left:127px;top:38px" width="120" height="120" viewBox="0 0 120 120"><path d="M100 30A52 52 0 1 0 110 60" fill="none" stroke="#fff" stroke-width="6"/><path d="M88 16 106 32 84 38z" fill="#fff"/><text x="57" y="70" text-anchor="middle" font-family="Saira, sans-serif" font-weight="700" font-size="32" fill="#fff">24/7</text></svg>
  <h3 class="abs head" style="color:#fff">24/7 MONITORING</h3>
  <p class="abs">Our team is always on guard. With always-on protection, we'll notify you of any suspicious activity. In emergencies, we'll monitor your local police, fire, or EMS.</p>
  <div class="abs btn-red" style="left:833px;top:77px;width:174px;height:42px">CONTACT US</div>
</section>

<!-- steps -->
<h2 class="abs head steps-h">CONNECT +<br>PROTECT YOUR WORLD</h2>
<div class="abs step" style="top:1800px"><div class="num" style="background:var(--red)">01</div><div><h5>BUILD AN INSTANT QUOTE</h5><p>Our live-estimate builder will guide you through a few<br>questions to help us understand your needs.</p><a href="#quote">GET STARTED</a></div></div>
<div class="abs step" style="top:1898px"><div class="num" style="background:var(--navy)">02</div><div><h5>BUILD A SCHEDULE INSTALLATION INSTANT QUOTE</h5><p>Our trained techs are efficient and friendly. Southern-born and raised (and one mid-westerner), we will respect your home and your schedule.</p></div></div>
<div class="abs step" style="top:1993px"><div class="num" style="background:var(--sky)">03</div><div><h5>STAY SECURE 24/7</h5><p>Monitor your home through the app, receive instant alerts, and rely on professional monitoring services for emergencies.</p></div></div>

<!-- founder -->
<section class="abs founder">
  <h2 class="abs head">I FOUNDED SILVER HERON SYSTEMS TO BRING TOGETHER TECHNOLOGY AND HONEST, RELIABLE SERVICE.</h2>
  <p class="abs">I'm proud to call Tennessee home and even prouder to help keep its homes and businesses secure. Whether it's protecting or elevating your space, my goal is to make technology work for you. Think of us as your friendly, neighborhood tech expert—here to safeguard what matters most.</p>
  <div class="abs sig" role="img" aria-label="Handwritten signature of founder Marcus Bell"></div>
  <svg class="abs" style="left:700px;top:45px" width="334" height="466" viewBox="0 0 334 466">
    <path d="M0 95 Q167 60 334 95 L334 270 Q334 390 167 466 Q0 390 0 270Z" fill="var(--red)"/>
    <path d="M334 300 L334 330 Q310 420 167 466 Q300 400 334 300Z" fill="var(--navy)"/>
    <path d="M0 300 Q10 400 167 466 Q0 390 0 270Z" fill="var(--navy)"/>
  </svg>
  <div class="abs portrait" role="img" aria-label="Portrait of founder Marcus Bell in suit and bow tie"></div>
</section>

<!-- testimonials -->
<svg class="abs" style="left:0;top:2734px" width="230" height="710" viewBox="0 0 230 710">
  <polygon points="0,0 120,0 230,150 0,480" fill="#eaf6fb"/>
  <polygon points="0,0 120,0 230,150 200,150 95,20 0,150" fill="var(--red)"/>
  <polygon points="0,150 95,20 200,150 150,150 0,400" fill="var(--red)"/>
  <polygon points="150,150 200,150 0,710 0,560" fill="var(--navy)"/>
</svg>
<h2 class="abs head sec-title" style="top:2830px">TESTIMONIALS SILVER HERON</h2>
<div class="abs t-card">
  <div class="abs t-left">
    <div style="margin-top:120px;display:flex;justify-content:center;align-items:center;gap:10px"><i style="display:block;width:18px;height:18px;border-radius:50%;background:var(--blue-mid)"></i><span style="font-family:Poppins,sans-serif;font-weight:600;font-size:40px;color:var(--blue-mid)">ReviewHub</span></div>
    <div style="font-size:15px;font-weight:500;margin-top:8px;color:#222">5 STAR CUSTOMER RATING</div>
    <div class="stars" style="font-size:24px;line-height:28px">★★★★★</div>
    <div style="font-size:10px;font-weight:600;margin-top:10px">READ REVIEWS</div>
  </div>
  <div class="abs t-right">
    <div class="abs t-inner"></div>
    <div class="abs quote-box">“</div>
    <div class="abs stars" style="left:79px;top:62px;font-size:13px">★★★★★</div>
    <p class="abs t-text">I couldn't be more impressed with the service we received for our condo's security system upgrade. The team was professional, efficient, and incredibly knowledgeable, providing us with state-of-the-art solutions that have significantly enhanced the safety and security of our building. Highly recommend their services!</p>
    <div class="abs" style="left:79px;top:313px;font-size:9.5px;font-weight:700;color:#fff;display:flex;align-items:center;gap:8px"><i style="display:block;width:26px;height:1px;background:#fff"></i>NORTHGATE PROPERTY GROUP</div>
  </div>
</div>

<!-- request a quote -->
<h2 class="abs head sec-title" id="quote" style="top:3370px">REQUEST A QUOTE</h2>
<div class="form">
  <label style="left:289px;top:3428px">Name</label>
  <div class="field" style="left:289px;top:3456px;width:300px;height:40px"></div>
  <label style="left:611px;top:3428px">Email <span style="color:var(--red)">*</span></label>
  <div class="field" style="left:611px;top:3456px;width:300px;height:40px"></div>
  <label style="left:289px;top:3508px">Phone</label>
  <div class="field" style="left:289px;top:3536px;width:622px;height:40px"></div>
  <label style="left:289px;top:3586px">Message</label>
  <div class="field ph" style="left:289px;top:3613px;width:622px;height:158px">Your message</div>
  <div class="abs btn-red" style="left:524px;top:3786px;width:152px;height:42px">SUBMIT NOW</div>
</div>

<!-- partners -->
<h2 class="abs head sec-title" style="top:3897px">SERVICE PARTNERS</h2>
<p class="abs center" style="top:3948px;width:1200px;font-size:12px;color:#333">(Need to replace these placeholders with partner logos</p>
<div class="abs partner" style="left:96px;width:190px" role="img" aria-label="Partner badge"><i style="width:120px"></i></div>
<div class="abs partner" style="left:300px;width:191px" role="img" aria-label="Partner badge"><i style="width:150px;background:#333"></i></div>
<div class="abs partner" style="left:506px;width:189px" role="img" aria-label="Partner badge"><i style="width:110px;height:22px"></i></div>
<div class="abs partner" style="left:712px;width:183px" role="img" aria-label="Partner badge"><i style="width:140px;height:26px;background:#1d4fa3"></i></div>
<div class="abs partner" style="left:901px;width:196px" role="img" aria-label="Partner badge"><i style="width:110px;height:30px;background:#1f2a44"></i></div>

<!-- newsletter -->
<section class="abs news">
  <svg class="abs" style="left:0;top:0" width="1200" height="182" viewBox="0 0 1200 182"><g fill="var(--red-dark)"><polygon points="0,0 60,0 0,120"/><polygon points="0,182 140,0 200,0 60,182"/><polygon points="1080,182 1200,20 1200,100 1140,182"/></g></svg>
  <h2 class="abs head">SUBSCRIBE TO OUR<br>NEWSLETTER</h2>
  <p class="abs">Security Tips, Special Offers, and More!</p>
  <div class="abs" style="left:688px;top:72px;width:260px;height:47px;background:#fff;font-size:11px;color:#777;padding:16px 26px">Your Email</div>
  <div class="abs" style="left:948px;top:72px;width:109px;height:47px;background:var(--blue-mid);color:#fff;font-size:12.5px;font-weight:700;display:flex;align-items:center;justify-content:center">SIGN UP</div>
</section>

<!-- footer -->
<footer class="abs footer">
  <div class="abs" style="left:105px;top:140px;width:200px;display:flex;align-items:center;gap:10px;font-weight:700;font-size:22px;line-height:26px">
    <i style="display:block;width:20px;height:20px;background:#fff;flex:none"></i><span>SILVER HERON SYSTEMS</span>
  </div>
  <div class="abs fcol" style="left:392px"><h6>RESIDENTIAL</h6><a>Home</a><a>Electronic Security</a><a>Audio + Video</a><a style="line-height:14px;margin:3px 0 4px">Networking +<br>Communication</a><a>Cabling</a></div>
  <div class="abs fcol" style="left:577px"><h6>RESIDENTIAL</h6><a>Home Security</a><a>Smart Homes</a><a>Home Theatres + A/V</a><a>WiFi</a><a>Cabling</a></div>
  <div class="abs fcol" style="left:741px"><h6>COMMERCIAL</h6><a>Audio Video</a><a>Cabling</a><a>Communication</a><a>Electronic Security</a><a>Project Consulting</a></div>
  <div class="abs fcol" style="left:917px;width:220px"><h6>CONTACT US</h6>
    <div style="position:relative;padding-left:22px;line-height:14px"><svg style="position:absolute;left:0;top:0" width="11" height="14" viewBox="0 0 24 30"><path fill="var(--red)" d="M12 0a11 11 0 0 0-11 11c0 8 11 19 11 19s11-11 11-19A11 11 0 0 0 12 0zm0 15a4 4 0 1 1 0-8 4 4 0 0 1 0 8z"/></svg><b style="font-size:12px">MAIN OFFICE:</b><br>412 Meridian Dr. Suite 2-108<br>Hendersonville, TN 37075</div>
    <div style="position:relative;padding-left:22px;line-height:14px;margin-top:8px"><b style="font-size:12px">CALL US:</b><br><svg style="position:absolute;left:0;top:15px" width="11" height="11" viewBox="0 0 24 24"><path fill="var(--red)" d="M6.6 10.8a15.1 15.1 0 0 0 6.6 6.6l2.2-2.2c.3-.3.7-.4 1-.2 1.1.4 2.3.6 3.6.6.6 0 1 .4 1 1V20c0 .6-.4 1-1 1C10.6 21 3 13.4 3 4c0-.6.4-1 1-1h3.5c.6 0 1 .4 1 1 0 1.3.2 2.5.6 3.6.1.3 0 .7-.2 1z"/></svg>615.555.0142</div>
  </div>
  <div class="abs" style="left:88px;top:331px;font-size:11px">©2024 Silver Heron Systems. All rights reserved.</div>
  <div class="abs" style="left:951px;top:331px;font-size:11px">Site Terms | Privacy Policy</div>
  <div class="abs" style="left:1128px;top:297px;width:40px;height:40px;border-radius:50%;background:var(--red);display:flex;align-items:center;justify-content:center"><svg width="10" height="7" viewBox="0 0 10 7"><path d="M1 6 5 2l4 4" fill="none" stroke="#fff" stroke-width="2"/></svg></div>
</footer>

</body>
</html>
```